Velto Web Design Project

We need a web design for a research project in Tuscany, Italy regarding trash collection in industrial sites using innovative garbage bin. Those innovative bin can communicate in wireless way their status and reserve their emptying to the operating trash company. To the other side the project give to trash company a logistic system in order to plan emptying operations aiming to optimize vehicles routing.

At this link you can find the logo of the project, previously realized and not changeble.

http://www.progetto-velto.example/velto/resources/logo_web.png

Industry/Entity Type

It Company

```html
<!DOCTYPE html>
<html lang="it">
<head>
<meta charset="utf-8">
<title>Velto</title>
<link href="https://fonts.googleapis.com/css2?family=Questrial&display=swap" rel="stylesheet">
<style>
:root{
  --top-bar:#1d1816;
  --band:#1e1816;
  --page:#efefef;
  --card:#ffffff;
  --green:#4e8a08;
  --logo-green:#8cc63f;
  --ink:#1a1a1a;
  --body:#4a4a4a;
  --pill:#2b2b2b;
  --pill-text:#9acd32;
}
*{margin:0;padding:0;box-sizing:border-box}
html,body{width:1053px;height:1200px;overflow:hidden}
body{background:var(--page);font-family:"Questrial",sans-serif;color:var(--body);position:relative}
.top-bar{position:absolute;left:0;top:0;width:1053px;height:8px;background:var(--top-bar)}
.site-header{position:absolute;left:0;top:8px;width:1053px;height:129px;background:linear-gradient(#e6e6e6,#f2f2f2)}
.brand{position:absolute;left:46px;top:26px;display:flex;align-items:center;gap:12px}
.brand-dot{width:30px;height:30px;border-radius:50%;background:var(--logo-green)}
.brand-name{font-size:50px;color:var(--ink);letter-spacing:1px}
.main-nav{position:absolute;top:77px;right:40px;display:flex;gap:4px}
.main-nav a{display:block;padding:7px 12px;font-size:15.8px;color:var(--ink);text-decoration:none;border-radius:5px}
.main-nav a.active{background:var(--pill);color:var(--pill-text);padding:7px 15px}
.hero-band{position:absolute;left:0;top:137px;width:1053px;height:398px;background:var(--band)}
.hero-photo{position:absolute;left:21px;top:145px;width:1011px;height:354px;border-radius:5px;
  background:linear-gradient(90deg,#8a918d 0%,#c9cbc7 22%,#e9e9e6 32%,#4a4fc2 44%,#3c42b8 62%,#c2c6c8 72%,#d6d8d8 100%)}
.content-card{position:absolute;left:21px;top:514px;width:1011px;height:634px;background:var(--card);border-radius:5px;box-shadow:0 1px 4px rgba(0,0,0,.15)}
.section{position:absolute}
.section h2{font-weight:400;font-size:21px;line-height:25px;color:var(--green);margin-left:4px;margin-bottom:6px}
.section p{font-size:12.2px;line-height:25.3px;text-align:justify}
.view-more{position:absolute;right:0;font-size:15px;line-height:18px;color:var(--green);text-decoration:none}
.intro{left:29px;top:24px;width:953px}
.intro .view-more{top:246px}
.contesto{left:28px;top:316px;width:340px}
.obiettivi{left:407px;top:316px;width:340px}
.col-text{margin-top:8px}
.contesto .view-more,.obiettivi .view-more{top:266px}
.partners{left:771px;top:316px;width:236px;height:300px}
.partner-badges{position:absolute;left:0;top:0;width:236px;height:300px}
.badge{position:absolute;border-radius:2px}
.b1{left:5px;top:44px;width:188px;height:72px;background:#d9dcdf}
.b2{left:5px;top:147px;width:105px;height:21px;background:#3f3f44}
.b3{left:126px;top:141px;width:91px;height:30px;background:#dde0f0}
.b4{left:0;top:200px;width:100px;height:57px;background:#f1ead0}
.b5{left:114px;top:205px;width:116px;height:41px;background:#e63b1e}
.footer-note{position:absolute;right:36px;top:1162px;font-size:13px;color:var(--ink)}
</style>
</head>
<body>
<div class="top-bar"></div>
<header class="site-header">
  <div class="brand"><span class="brand-dot"></span><span class="brand-name">VELTO</span></div>
  <nav class="main-nav">
    <a class="active" href="#">Il Progetto!</a>
    <a href="#">Partners!!</a>
    <a href="#">Materiale!</a>
    <a href="#">Links</a>
    <a href="#">Gli appuntamenti</a>
    <a href="#">Area Protetta</a>
  </nav>
</header>
<div class="hero-band"></div>
<div class="hero-photo" role="img" aria-label="Fila di cassonetti per la raccolta differenziata: verdi, bianchi, blu per la carta e grigi per il vetro"></div>
<main class="content-card">
  <section class="section intro">
    <h2>Introduzione</h2>
    <p>Il progetto ha come obiettivo la progettazione e sviluppo sperimentale di una piattaforma di servizi di infomobilità e tracciamento per la raccolta e trasporto dei rifiuti speciali. La piattaforma è distinta in due componenti principali: una componente periferica, costituita da tecnologie di identificazione e sensoristica per l'acquisizione in tempo reale di dati utili per il controllo e monitoraggio dei rifiuti speciali e dei veicoli addetti al trasporto, ed un Centro Servizi che ospita la logica applicativa per l'integrazione dei dati acquisiti e per i servizi applicativi di gestione delle flotte e tracciamento dei rifiuti nelle fasi di raccolta e trasporto. Un'architettura di questo genere consente l'ottimizzazione della raccolta e del trasporto fornendo una base dati completa che traccia ogni carico dal punto di partenza al punto di arrivo; in questo modo, il processo risulta interamente automatizzato, poiché consente sia di identificare - qualitativamente e quantitativamente - il carico raccolto e trasportato, sia di eliminare i possibili errori operativi che possono insorgere lungo i percorsi dei mezzi addetti alla raccolta (minimizzando la frequenza dei giri di raccolta), sia di rendere impossibile la manipolazione della classificazione della merce raccolta, operando un diverso smaltimento da quello previsto, ad es. allo scopo di ottenere guadagni illeciti.</p>
    <a class="view-more" href="#">View more</a>
  </section>
  <section class="section contesto">
    <h2>Contesto</h2>
    <p class="col-text">Il settore della gestione dei rifiuti speciali è caratterizzato da una forte complessità gestionale ed operativa. Il mercato deve consentire un incontro efficace ed efficiente fra domanda ed offerta, garantendo da un lato la capillarità delle reti di raccolta dei rifiuti presso i produttori e dall'altro assicurando in tempi definiti il conferimento dei materiali raccolti presso molteplici filiere di trattamento, recupero e smaltimento.</p>
    <a class="view-more" href="#">View more</a>
  </section>
  <section class="section obiettivi">
    <h2>Obiettivi</h2>
    <p class="col-text">Il settore della gestione dei rifiuti speciali è caratterizzato da una forte complessità gestionale ed operativa. Il mercato deve consentire un incontro efficace ed efficiente fra domanda ed offerta, garantendo da un lato la capillarità delle reti di raccolta dei rifiuti presso i produttori e dall'altro assicurando in tempi definiti il conferimento dei materiali raccolti presso molteplici filiere di trattamento, recupero e smaltimento.</p>
    <a class="view-more" href="#">View more</a>
  </section>
  <section class="section partners">
    <h2>Our Partners</h2>
    <div class="partner-badges">
      <span class="badge b1"></span>
      <span class="badge b2"></span>
      <span class="badge b3"></span>
      <span class="badge b4"></span>
      <span class="badge b5"></span>
    </div>
  </section>
</main>
<footer class="footer-note">2012 © copyrights.velto.received</footer>
</body>
</html>
```